Lumen Botanicals Label Project- Updates made to project!

Project Scope: Branding opportunity for internet based skin care line. Design coordinating label for 4 different products. Each design shall be editable in Adobe Illustrator as a template including all fonts, symbols, and guides. Submit a design for all 4 products (preferably together as it would look on a retail shelf), business card, and logo.
Cleanser: STEP 1 Label Size: 5 x 4.5 inches (w x h) CALM CLEANSER
Toner: STEP 2 Label Size: 5 x 4.5 inches (w x h) TRANQUIL TONER- A piece of each crystal sits at the bottom of each solution. It coordinates with the "Quiet Heart" of our logo.
Serum STEP 3 Label Size: Label Size: 4.25 x 2.25 ANTI-AGING SERUM
Moisturizer: STEP 4 Label Size: Label Size: 1”x7.25” MOISTURIZER
Each label needs to include:
Front:
Attractive larger sized STEP #
Logo
Product name and short description
Decorative design Symbol(s)
Back:
Area on back to say short description
Directions for use
Larger area for ingredients
Website: www.lumenbotanicals-example.com
Address of distribution
Barcode

Lumen Skin Care, an esthetician created line provides organic and natural based products for all skin types. With an emphasis on anti-aging, this simple 4- step system can be used by many including pregnant and oncology consumers. The unique thing about our line is that the toners and serums contain crystals such as amethyst and rose quarts to promote Quiet Heart as well as outer beauty. Each product is handmade with natural, quality ingredients and are 70-90% Organic.
Target Market: Women ages 30-45 years old. This demographic is on the go, and wants a simple-easy to read label, & a skin care system that addresses her concerns. Just as this consumer is mindful of her fitness and what she puts in her body, she tends to purchase environmentally friendly, and natural products. Health and wellness trends reflect this, as organic beauty products are expected to grow 74% from 2013 to 2018. She enjoys meditation and yoga, and she is curious about eastern medicine holistic healing trends.

Company Name: Lumen Skin Care
Tagline: Quiet Heart- Bright Face
Package Feel: Simple, elegant easy to read step on each product. STEP 1: AM/PM. Attractive numbering. A symbol that reflects the brand. Not necessarily a Lumen or Crystal because the name speaks for itself. Beautiful, soft, eye catching design that draws the consumer to pick it up. Clear or white label welcomed. Some color palettes provided.
Descriptive words the packaging should represent: Yoga, Zen, mystic, eye catching, healing energy, natural, quality ingredients, sophisticated, beautiful, serenity, easy to read- bold-attractive numbering on front.
Inspiration Brands: VARLA Organics- Beautiful watercolor packaging that resonates a "feeling"

Attached are pictures of the packaging, inspirational pictures, skin care lines that are attractive, ect.

Packaging SPECS:

Cleanser:
Color Clear
Size 4 oz
Material PET
Case Pack
Neck Finish 24-410
Diameter 1.58 in / 4.013 cm
Height 6 in / 15.240 cm
Label Dimensions 5x4.5
Print Dimensions 5x4.5
Print Dimensions in (diameter)

TONER BOTTLE: Same as above

SERUM BOTTLE:
Color Clear
Size 2 oz
Material PET
Neck Finish 20-410
Diameter 1.358 in / 3.449 cm
Height 3.274 in / 8.316 cm

Moisturizer:
2.3 oz
Height:53 mm
Diameter: 60 mm
Neck: 58/400

Target Market(s)

Women ages 30-45 years old. This demographic is on the go, and wants a simple-easy to read label, & a skin care system that addresses her concerns. Just as this consumer is mindful of her fitness and what she puts in her body, she tends to purchase environmentally friendly, and natural products. Health and wellness trends reflect this, as organic beauty products are expected to grow 74% from 2013 to 2018. She enjoys meditation and yoga, and she is curious about eastern medicine holistic healing trends.

Industry/Entity Type

Skin Care Product

Contact Information for Business Card

Details given upon completion.

Logo Text

Lumen Botanicals Quiet Heart- Bright Face

Requirements
Must have
• A large step number on the front. Coordinating symbols and colors. Must have a professional retail look and be easy to read.
Nice to have
• Clean, simple, eye catching packaging. Watercolor designs. Designs that inspire "feelings" www.varlaorganics-example.com

```html
<!DOCTYPE html>
<html lang="en">
<head>
<meta charset="utf-8">
<title>Lumen Skin Care – Label Set</title>
<link href="https://fonts.googleapis.com/css2?family=Cormorant+Garamond:ital,wght@0,400;0,500;0,600;1,400&family=Lato:wght@400;700&display=swap" rel="stylesheet">
<style>
  :root{
    --paper:#ffffff;
    --frame:#9c9c9c;
    --silver:#9a9a9a;
    --silver-dark:#7d7d7d;
    --ink:#4a4a4a;
    --lilac:rgba(142,98,178,0.72);
    --lilac-soft:rgba(170,130,200,0.45);
    --veil:rgba(245,243,247,0.82);
    --rule:#b9b9b9;
  }
  *{box-sizing:border-box;margin:0;padding:0}
  html,body{width:1061px;height:1200px;overflow:hidden;background:var(--paper)}
  body{position:relative;font-family:"Cormorant Garamond",Georgia,serif;color:var(--ink)}

  .label{position:absolute;border:1px solid var(--frame);background:var(--paper);overflow:hidden}
  .label--cleanser{left:25px;top:40px;width:490px;height:440px}
  .label--toner{left:546px;top:40px;width:490px;height:440px}
  .label--serum{left:25px;top:530px;width:424px;height:225px}
  .label--moisturizer{left:25px;top:810px;width:1011px;height:140px}

  .wash{position:absolute;border-radius:50%;filter:blur(6px)}
  .wash--top{background:radial-gradient(ellipse at 50% 50%,var(--lilac) 0%,var(--lilac-soft) 45%,rgba(200,170,220,0) 72%)}
  .wash--side{background:radial-gradient(ellipse at 50% 50%,var(--lilac) 0%,var(--lilac-soft) 40%,rgba(200,170,220,0) 70%)}

  .front{position:absolute;background:var(--veil);text-align:center;display:flex;flex-direction:column;align-items:center}
  .brand{display:flex;flex-direction:column;align-items:center}
  .brand__mark{border:1.5px solid var(--silver);border-radius:50%}
  .brand__name{letter-spacing:.45em;color:var(--silver);font-weight:500;padding-left:.45em}
  .brand__sub{font-family:"Lato",sans-serif;letter-spacing:.3em;color:var(--silver);padding-left:.3em}
  .step{font-weight:500;color:var(--silver);line-height:1;background:linear-gradient(180deg,#c4c4c4,var(--silver-dark));-webkit-background-clip:text;background-clip:text;-webkit-text-fill-color:transparent}
  .product{font-family:"Lato",sans-serif;letter-spacing:.16em;color:var(--silver-dark);font-weight:700}
  .dot{color:var(--silver-dark)}
  .tagline{font-style:italic;color:var(--silver);letter-spacing:.05em;line-height:1.45}

  .back{position:absolute;font-size:8px;line-height:1.3;color:var(--ink)}
  .back__mark{border:1.5px solid var(--silver-dark);border-radius:50%;margin:0 auto 10px}
  .back__title{font-weight:600;letter-spacing:.12em;padding-bottom:4px;border-bottom:1px solid var(--rule);margin-bottom:4px}
  .back__block{padding-bottom:5px;border-bottom:1px solid var(--rule);margin-bottom:5px}
  .back__head{letter-spacing:.12em}
  .website{font-family:"Lato",sans-serif;color:var(--silver-dark);letter-spacing:.04em;margin-top:14px}

  /* large labels */
  .label--cleanser .front,.label--toner .front{left:47px;top:37px;width:153px;height:283px;padding-top:28px}
  .label--cleanser .brand__mark,.label--toner .brand__mark{width:26px;height:26px;margin-bottom:10px}
  .label--cleanser .brand__name,.label--toner .brand__name{font-size:15px}
  .label--cleanser .brand__sub,.label--toner .brand__sub{font-size:5px;margin-top:1px}
  .label--cleanser .step,.label--toner .step{font-size:88px;margin-top:8px}
  .label--cleanser .product,.label--toner .product{font-size:10px;margin-top:6px}
  .label--cleanser .dot,.label--toner .dot{font-size:9px;margin:6px 0 4px}
  .label--cleanser .tagline,.label--toner .tagline{font-size:10.5px}
  .label--cleanser .back,.label--toner .back{left:309px;top:104px;width:118px}
  .label--cleanser .back__mark,.label--toner .back__mark{width:26px;height:26px}

  /* serum */
  .label--serum .front{left:40px;top:15px;width:112px;height:185px;padding-top:14px}
  .label--serum .brand__mark{width:16px;height:16px;margin-bottom:5px}
  .label--serum .brand__name{font-size:10px}
  .label--serum .brand__sub{font-size:4px}
  .label--serum .step{font-size:56px;margin-top:4px}
  .label--serum .product{font-size:7.5px;margin-top:3px}
  .label--serum .dot{font-size:7px;margin:3px 0 2px}
  .label--serum .tagline{font-size:7px}
  .label--serum .back{left:198px;top:16px;width:165px;font-size:6.5px}
  .label--serum .back__title{text-align:center}
  .label--serum .website{text-align:center;font-size:7px;margin-top:10px}

  /* moisturizer */
  .label--moisturizer .front{left:95px;top:32px;width:230px;height:80px;background:transparent;flex-direction:row;align-items:center;text-align:left}
  .label--moisturizer .step{font-size:72px;margin-right:16px}
  .mo-text{display:flex;flex-direction:column}
  .mo-brand{display:flex;align-items:center;gap:6px}
  .label--moisturizer .brand__mark{width:20px;height:20px}
  .label--moisturizer .brand__name{font-size:13px}
  .label--moisturizer .brand__sub{font-size:4.5px;padding-left:0;margin-left:30px}
  .label--moisturizer .product{font-size:13px;letter-spacing:.06em;margin-top:4px}
  .label--moisturizer .tagline{font-size:8.5px}
  .label--moisturizer .back{left:524px;top:26px;width:286px;font-size:6.5px}
  .label--moisturizer .website{position:absolute;right:22px;bottom:14px;font-size:8px}
</style>
</head>
<body>

<!-- Step 1 -->
<section class="label label--cleanser">
  <div class="wash wash--top" style="left:190px;top:-120px;width:330px;height:230px" role="img" aria-label="Purple watercolour wash"></div>
  <div class="wash wash--side" style="left:-90px;top:300px;width:300px;height:230px" role="img" aria-label="Purple watercolour wash"></div>
  <div class="wash wash--side" style="left:430px;top:320px;width:120px;height:180px" role="img" aria-label="Purple watercolour wash"></div>
  <div class="front">
    <div class="brand"><span class="brand__mark"></span><span class="brand__name">LUMEN</span><span class="brand__sub">SKIN CARE</span></div>
    <div class="step">1</div>
    <div class="product">CALM CLEANSER</div>
    <div class="dot">✦</div>
    <div class="tagline">Hydrating,<br>age defying formula</div>
  </div>
  <div class="back">
    <div class="back__mark"></div>
    <div class="back__title">SHORT DESCRIPTION</div>
    <div class="back__block"><div class="back__head">DIRECTIONS FOR USE</div>Apply to damp skin, massage gently, rinse well.</div>
    <div class="back__block">Ingredients: aloe leaf juice, rose water, jojoba oil, glycerin, chamomile extract, green tea, vitamin E, lavender oil, amethyst essence.</div>
    <div>Address of distribution: 12 Willow Lane, Springfield 00000</div>
    <div class="website">www.lumen-skincare-example.com</div>
  </div>
</section>

<!-- Step 2 -->
<section class="label label--toner">
  <div class="wash wash--top" style="left:190px;top:-120px;width:330px;height:230px" role="img" aria-label="Purple watercolour wash"></div>
  <div class="wash wash--side" style="left:-90px;top:300px;width:300px;height:230px" role="img" aria-label="Purple watercolour wash"></div>
  <div class="wash wash--side" style="left:430px;top:320px;width:120px;height:180px" role="img" aria-label="Purple watercolour wash"></div>
  <div class="front">
    <div class="brand"><span class="brand__mark"></span><span class="brand__name">LUMEN</span><span class="brand__sub">SKIN CARE</span></div>
    <div class="step">2</div>
    <div class="product">TRANQUIL TONER</div>
    <div class="dot">✦</div>
    <div class="tagline">Hydrating,<br>age defying formula</div>
  </div>
  <div class="back">
    <div class="back__mark"></div>
    <div class="back__title">SHORT DESCRIPTION</div>
    <div class="back__block"><div class="back__head">DIRECTIONS FOR USE</div>Sweep over clean skin with a soft pad.</div>
    <div class="back__block">Ingredients: aloe leaf juice, rose water, witch hazel, glycerin, chamomile extract, green tea, vitamin E, lavender oil, quartz essence.</div>
    <div>Address of distribution: 12 Willow Lane, Springfield 00000</div>
    <div class="website">www.lumen-skincare-example.com</div>
  </div>
</section>

<!-- Step 3 -->
<section class="label label--serum">
  <div class="wash wash--top" style="left:110px;top:-80px;width:280px;height:140px" role="img" aria-label="Purple watercolour wash"></div>
  <div class="wash wash--side" style="left:-60px;top:150px;width:200px;height:130px" role="img" aria-label="Purple watercolour wash"></div>
  <div class="wash wash--side" style="left:370px;top:140px;width:90px;height:120px" role="img" aria-label="Purple watercolour wash"></div>
  <div class="front">
    <div class="brand"><span class="brand__mark"></span><span class="brand__name">LUMEN</span><span class="brand__sub">SKIN CARE</span></div>
    <div class="step">3</div>
    <div class="product">ANTI-AGING SERUM</div>
    <div class="dot">✦</div>
    <div class="tagline">Hydrating,<br>age defying formula</div>
  </div>
  <div class="back">
    <div class="back__title">SHORT DESCRIPTION</div>
    <div class="back__block">DIRECTIONS FOR USE: Press two drops into face morning and night.</div>
    <div class="back__block">Ingredients: rosehip oil, hyaluronic acid, aloe leaf juice, argan oil, vitamin C, vitamin E, green tea, frankincense, amethyst essence.</div>
    <div>Address of distribution: 12 Willow Lane, Springfield 00000</div>
    <div class="website">www.lumen-skincare-example.com</div>
  </div>
</section>

<!-- Step 4 -->
<section class="label label--moisturizer">
  <div class="wash wash--top" style="left:480px;top:-60px;width:420px;height:120px" role="img" aria-label="Purple watercolour wash"></div>
  <div class="wash wash--side" style="left:-60px;top:30px;width:240px;height:150px" role="img" aria-label="Purple watercolour wash"></div>
  <div class="wash wash--side" style="left:940px;top:-20px;width:120px;height:200px" role="img" aria-label="Purple watercolour wash"></div>
  <div class="front">
    <div class="step">4</div>
    <div class="mo-text">
      <div class="mo-brand"><span class="brand__mark"></span><span class="brand__name">LUMEN</span></div>
      <span class="brand__sub">SKIN CARE</span>
      <div class="product">MOISTURIZER</div>
      <div class="tagline">Hydrating, age defying formula</div>
    </div>
  </div>
  <div class="back">
    <div class="back__title" style="border:none;margin:0;padding:0">SHORT DESCRIPTION</div>
    <div class="back__block">DIRECTIONS FOR USE: Smooth over face and neck after serum.</div>
    <div class="back__block">Ingredients: shea butter, aloe leaf juice, jojoba oil, glycerin, squalane, rose water, vitamin E, calendula, lavender oil, quartz essence.</div>
    <div>Address of distribution: 12 Willow Lane, Springfield 00000</div>
  </div>
  <div class="website">www.lumen-skincare-example.com</div>
</section>

</body>
</html>
```